Boutique Salon Brand Refresh needs color palette, font, templates.

Lorvu Hair Design is an established hair salon celebrating 10 years in business. We are currently evolving our brand to better reflect who we are today, the clients we serve, and the direction we want to take our business moving forward.
Our goal is to position Lorvu as a refined, modern boutique salon created specifically for “The Lorvu Woman.”
In the past, much of our branding and marketing focused on us—our salon, our space, our services, and our team. Going forward, we want to shift that focus to her: who she is, what she values, how she wants to look and feel, and how Lorvu fits into her life.
We want our brand to communicate expertise and quality without feeling overly luxurious, trendy, intimidating, or impersonal. It should feel polished, sophisticated, warm, approachable, and timeless—a boutique experience designed for women who value beautiful, healthy hair and trusted professional guidance.
As part of this rebrand, we are looking to establish a cohesive visual identity that can be carried consistently across our website, social media, email marketing, print materials, signage, and other client touchpoints.

*** For THIS PROJECT, we are SPECIFICALLY LOOKING for:
- A cohesive brand color palette
- 2–3 complementary fonts for consistent use across our marketing
- 4–5 customizable social media templates that can be used across Instagram and Facebook
A visual direction that feels distinctive to Lorvu and speaks directly to The Lorvu Woman.
The following information provides more detail about The Lorvu Woman, our positioning, brand personality, values, and the overall direction we envision for the next chapter of Lorvu Hair Design.
Lorvu Hair Design
Mendham, NJ USA
lorvuhairstudio.example

--PRIMARY AUDIENCE
The Lorvu woman values quality, consistency, and professional guidance.
She wants to look polished and current without appearing overdone or overly trendy.
She may be managing grey hair, changing texture, thinning, dryness, fading color, or a style that no longer reflects who she is. She wants an expert who understands these concerns and can create a realistic plan.
She is willing to invest in professional services and products when she understands their value.
She does not want to experiment with her appearance.
She wants to feel confident in the person caring for her hair.
Women approximately 45 to 65 years old living in Mendham, Morris County, and surrounding communities.

--COLOR PALETTE
The overall appearance should feel calm, spacious, editorial, and cohesive. The entire visual system should feel more like a refined boutique hotel, skincare brand, or luxury lifestyle publication than a traditional salon advertisement.
When choosing the palette, we want the colors to invoke these feelings.
Represents:
Expertise
Confidence
Timelessness
Professionalism
Calm
Warmth
Cleanliness
Soft luxury
Natural beauty
Warmth
Balance
Subtle sophistication
Consistency

--TYPOGRAPHY
The typography system should feel refined, modern, readable, and timeless.
Recommended usage for each font, size, spacing, etc.

----TEMPLATE IDEAS
**EDUCATIONAL POST
Frequently asked questions
Healthy-hair advice
Healthy Hair Tip
Grey Coverage FAQ
Grey Blending FAQ
Product education
Single-tip graphic
**REVIEWS
Google reviews
Finest in Town recognition/Community awards
Long-term guest relationships
Guest testimonials/satisfaction stories
Referral stories
**ADS
**SALON UPDATES/INFO
Holiday hours
Policy reminder
New guest guide
Consultation invitation
Service spotlight
Seasonal guidance
**ABOUT LORVU
Who we are
What to expect from us
What we can provide
Our expertise
**HIGHLIGHT ICON
Questions
Testimonial
Product
Reminders

TEMPLATE RULES
Use the color palette
Use only the font system
Maintain generous spacing
Limit text
Use consistent margins
Keep calls to action simple
Avoid crowded layouts
Use photography intentionally
Keep every template recognizably Lorvu

Target Market(s)

Women approximately 45 to 65 years old living in Mendham, Morris County, and surrounding communities. She values quality, consistency, and professional guidance. She wants to look polished and current without appearing overdone or overly trendy. She is willing to invest in professional services and products when she understands their value.

Industry/Entity Type

Hair Salon

Font styles to use
Serif
Sans Serif
Script

Requirements
Must have
• We are looking to establish a cohesive visual identity that can be carried consistently across platforms. It should communicate expertise and quality without feeling overly fluffy, trendy, intimidating, or impersonal. I would like to see multiple template ideas. Example- one template for education post, one template for reviews, one for salon information/updates. etc. My main goal here is to simplify social media posts by having designated templates for each post category. WE WILL BE KEEPING OUR ORGINAL LOGO- SO COLOR PALETTE MUST REFLECT THAT.
Nice to have
• Color palette and font sets that reflect the brand. **cohesive visual identity**
Should not have
• Nothing flashy, busy, overly trendy.

```html
<!DOCTYPE html>
<html lang="en">
<head>
<meta charset="utf-8">
<title>Lorvu Hair Design – Brand Identity Board</title>
<link rel="stylesheet" href="https://fonts.googleapis.com/css2?family=Alex+Brush&family=Montserrat:wght@400;500;600&family=Playfair+Display:ital,wght@0,400;0,500;0,700;1,400&display=swap">
<style>
  :root{
    --ivory:#f8f5f1;
    --linen:#ded6cc;
    --taupe:#bcae9e;
    --mauve:#b79a9b;
    --sage:#9eaa94;
    --charcoal:#383838;
    --mint:#eef3ea;
    --cream:#faf7f3;
    --rule:#a7a7a7;
    --serif:'Playfair Display', Georgia, serif;
    --sans:'Montserrat', Arial, sans-serif;
    --script:'Alex Brush', cursive;
  }
  *{box-sizing:border-box;margin:0;padding:0}
  html,body{width:1200px;height:1200px;overflow:hidden;background:#fff}
  .board{position:relative;width:1200px;height:1200px;color:var(--charcoal);font-family:var(--sans)}

  .section-title{position:absolute;font-family:var(--sans);font-weight:400;font-size:24px;letter-spacing:.5px;color:var(--charcoal)}
  .section-rule{position:absolute;height:2px;width:204px;background:var(--rule)}

  /* primary wordmark */
  .wordmark{position:absolute;left:40px;top:110px;width:320px;font-family:var(--serif);font-weight:400}
  .wordmark .name{display:block;font-size:130px;line-height:1;letter-spacing:-2px;color:var(--charcoal)}
  .wordmark .sub{display:block;font-size:27px;letter-spacing:.5px;margin-top:78px;text-transform:uppercase;color:var(--mauve)}

  .logo-tile{position:absolute;top:100px;width:266px;height:266px;border-radius:24px;display:flex;flex-direction:column;align-items:center;justify-content:center;color:#fff;font-family:var(--serif);font-weight:400}
  .logo-tile .name{font-size:64px;line-height:1;letter-spacing:-1px}
  .logo-tile .sub{font-size:15px;letter-spacing:1px;text-transform:uppercase;margin-top:10px}
  .tile-mauve{left:604px;background:var(--mauve)}
  .tile-charcoal{left:888px;background:var(--charcoal)}

  /* palette */
  .swatches{position:absolute;left:39px;top:483px;display:flex;gap:5.5px}
  .swatch{width:67px;height:67px;border-radius:6px}

  /* typography specimens */
  .specimen-glyph{position:absolute;left:36px;font-size:150px;line-height:1;color:var(--charcoal)}
  .specimen-name{position:absolute;left:243px;color:var(--charcoal)}
  .specimen-weights{position:absolute;left:243px;font-size:15px;color:var(--charcoal)}
  .specimen-body{position:absolute;left:243px;width:288px;color:var(--charcoal)}

  .g-serif{font-family:var(--serif)}
  .g-sans{font-family:var(--sans)}
  .g-script{font-family:var(--script)}

  /* post templates */
  .post{position:absolute;width:267px;height:267px;overflow:hidden;box-shadow:4px 6px 10px rgba(0,0,0,.18)}
  .post-logo{position:absolute;font-family:var(--serif);font-weight:400;line-height:1;text-align:left}
  .post-logo .name{display:block;font-size:26px;letter-spacing:-.5px}
  .post-logo .sub{display:block;font-size:4px;letter-spacing:.4px;text-transform:uppercase;margin-top:3px}
  .post-url{position:absolute;left:0;right:0;text-align:center;font-family:var(--sans);font-size:6.5px;letter-spacing:1.6px;white-space:nowrap}
  .photo{position:absolute}
  .flourish{position:absolute;border-radius:50%;opacity:.35}

  .tip-post{left:602px;top:491px;background:var(--cream)}
  .tip-label{position:absolute;left:13px;top:13px;width:128px;height:50px;background:var(--mauve);border-radius:3px;color:#fff;font-family:var(--serif);font-size:18.5px;line-height:19px;padding:6px 8px}
  .tip-rule{position:absolute;left:13px;top:70px;width:128px;height:1px;background:#d9cfcf}
  .tip-copy{position:absolute;left:13px;top:75px;width:112px;font-size:6.3px;line-height:8.6px;color:var(--charcoal)}

  .updates-post{left:887px;top:491px;background:var(--sage)}
  .updates-title{position:absolute;left:133px;width:134px;top:98px;text-align:center;font-family:var(--script);font-size:29px;line-height:28px;color:var(--charcoal)}
  .updates-meta{position:absolute;left:133px;width:134px;top:162px;text-align:center;font-size:5px;letter-spacing:.2px;color:#fff}
  .updates-url{left:133px;width:134px;right:auto;font-size:5.6px;letter-spacing:.6px}

  .rental-post{left:602px;top:776px}
  .rental-box{position:absolute;left:56px;top:97px;width:150px;height:73px;background:rgba(158,170,148,.8);border-radius:6px;display:flex;align-items:center;justify-content:center;text-align:center;font-family:var(--serif);font-style:italic;font-size:24px;line-height:26px;color:var(--charcoal)}
  .rental-band{position:absolute;left:0;right:0;top:241px;height:17px;background:rgba(158,170,148,.7)}

  .review-post{left:887px;top:776px;background:var(--mint)}
  .quote-box{position:absolute;left:55px;top:92px;width:156px;height:112px;background:var(--sage);border-radius:10px;color:#fff;text-align:center;padding:12px 12px 0}
  .quote-text{font-family:var(--serif);font-style:italic;font-size:7.4px;line-height:10.4px}
  .quote-stars{font-size:7px;letter-spacing:3px;margin-top:6px}
  .quote-rule{height:1px;background:rgba(255,255,255,.6);margin:5px 4px 6px}
  .quote-name{font-family:var(--sans);font-size:5.2px;letter-spacing:.2px;color:var(--charcoal)}
  .quote-mark{position:absolute;font-family:var(--serif);font-size:62px;line-height:1;color:var(--taupe)}
</style>
</head>
<body>
<div class="board">

  <h2 class="section-title" style="left:40px;top:30px">BRAND IDENTITY</h2>
  <div class="section-rule" style="left:40px;top:67px"></div>
  <div class="wordmark"><span class="name">Lorvu</span><span class="sub">Hair Design</span></div>

  <h2 class="section-title" style="left:604px;top:30px">LOGO VARIATIONS</h2>
  <div class="section-rule" style="left:604px;top:67px"></div>
  <div class="logo-tile tile-mauve"><span class="name">Lorvu</span><span class="sub">Hair Design</span></div>
  <div class="logo-tile tile-charcoal"><span class="name">Lorvu</span><span class="sub">Hair Design</span></div>

  <h2 class="section-title" style="left:40px;top:427px">COLOR PALETTE</h2>
  <div class="section-rule" style="left:40px;top:463px"></div>
  <div class="swatches">
    <div class="swatch" style="background:var(--ivory)"></div>
    <div class="swatch" style="background:var(--linen)"></div>
    <div class="swatch" style="background:var(--taupe)"></div>
    <div class="swatch" style="background:var(--mauve)"></div>
    <div class="swatch" style="background:var(--sage)"></div>
    <div class="swatch" style="background:var(--charcoal)"></div>
  </div>

  <h2 class="section-title" style="left:39px;top:598px">TYPOGRAPHY</h2>
  <div class="section-rule" style="left:39px;top:633px"></div>

  <div class="specimen-glyph g-serif" style="top:642px">Aa</div>
  <div class="specimen-name g-serif" style="top:652px;font-size:28px">Playfair Display</div>
  <div class="specimen-weights g-serif" style="top:691px">Regular / Medium / Bold</div>
  <p class="specimen-body g-serif" style="top:717px;font-size:8.3px;line-height:10.2px">Lorem ipsum dolor sit amet, consectetuer adipiscing elit, sed diam nonummy nibh euismod tincidunt ut laoreet dolore magna aliquam erat volutpat. Ut wisi enim ad minim veniam, quis nostrud exerci tation ullamcorper suscipit lobortis nisl ut aliquip ex ea commodo consequat. Duis autem vel eum iriure dolor in hendrerit in vulputate velit esse molestie consequat,</p>

  <div class="specimen-glyph g-sans" style="top:810px;font-size:140px">Aa</div>
  <div class="specimen-name g-sans" style="top:818px;font-size:27px">Montserrat</div>
  <div class="specimen-weights g-sans" style="top:856px">Regular / Medium / Bold</div>
  <p class="specimen-body g-sans" style="top:881px;font-size:8.2px;line-height:10.2px">Lorem ipsum dolor sit amet, consectetuer adipiscing elit, sed diam nonummy nibh euismod tincidunt ut laoreet dolore magna aliquam erat volutpat. Ut wisi enim ad minim veniam, quis nostrud exerci tation ullamcorper suscipit lobortis nisl ut aliquip ex ea commodo consequat. Duis autem vel eum iriure dolor in hendrerit in vulputate velit esse molestie consequat,</p>

  <div class="specimen-glyph g-script" style="top:975px;font-size:130px">Aa</div>
  <div class="specimen-name g-script" style="top:975px;font-size:28px">Alex Brush</div>
  <div class="specimen-weights g-script" style="top:1016px;font-size:13px">Regular</div>
  <p class="specimen-body g-script" style="top:1036px;font-size:7.2px;line-height:10px">Lorem ipsum dolor sit amet, consectetuer adipiscing elit, sed diam nonummy nibh euismod tincidunt ut laoreet dolore magna aliquam erat volutpat. Ut wisi enim ad minim veniam, quis nostrud exerci tation ullamcorper suscipit lobortis nisl ut aliquip ex ea commodo consequat. Duis autem vel eum iriure dolor in hendrerit in vulputate velit esse molestie consequat, vel illum dolore eu feugiat nulla facilisis at vero eros et accumsan et iusto odio dignissim</p>

  <h2 class="section-title" style="left:604px;top:425px">POST TEMPLATE</h2>
  <div class="section-rule" style="left:604px;top:463px"></div>

  <article class="post tip-post">
    <div class="tip-label">Healthy Hair<br>Tip</div>
    <div class="post-logo" style="left:205px;top:16px;color:var(--charcoal)"><span class="name" style="font-size:22px">Lorvu</span><span class="sub">Hair Design</span></div>
    <div class="tip-rule"></div>
    <p class="tip-copy">Apply a lightweight leave-in conditioner to damp mid-lengths and ends. Focus on the last three inches where moisture escapes fastest. Avoid the scalp to keep volume intact.</p>
    <div class="flourish" role="img" aria-label="Faint line flourish ornament" style="left:10px;top:165px;width:120px;height:70px;background:radial-gradient(ellipse,rgba(183,154,155,.25),transparent 70%)"></div>
    <div class="photo" role="img" aria-label="Photo of long brunette hair with soft balayage waves, seen from behind" style="left:143px;top:93px;width:110px;height:137px;background:linear-gradient(160deg,#d9d3cb 0%,#8a6a4c 35%,#c7a37a 65%,#3b3230 100%)"></div>
    <div class="post-url" style="top:249px;color:#a99c9c">www.lorvuhairstudio.example</div>
  </article>

  <article class="post updates-post">
    <div class="photo" role="img" aria-label="Photo of long straight caramel brown hair seen from behind, green plant in background" style="left:0;top:0;width:133px;height:267px;background:linear-gradient(180deg,#e9e6df 0%,#a6784d 25%,#b98b5d 60%,#8f6a48 100%)"></div>
    <div class="post-logo" style="left:174px;top:15px;color:#fff"><span class="name" style="font-size:24px">Lorvu</span><span class="sub">Hair Design</span></div>
    <div class="updates-title">Salon<br>Updates</div>
    <div class="updates-meta">NEW ARRIVALS &nbsp;|&nbsp; SEASONAL EDIT</div>
    <div class="flourish" role="img" aria-label="Faint line flourish ornament" style="left:145px;top:180px;width:115px;height:60px;background:radial-gradient(ellipse,rgba(255,255,255,.35),transparent 70%)"></div>
    <div class="post-url updates-url" style="top:249px;color:#fff">www.lorvuhairstudio.example</div>
  </article>

  <article class="post rental-post">
    <div class="photo" role="img" aria-label="Photo of long wavy hair with golden blonde ends in a bright salon" style="left:0;top:0;width:267px;height:267px;background:linear-gradient(180deg,#d9c8b4 0%,#8e6247 30%,#b5835a 60%,#d7ae78 85%,#c49a6a 100%)"></div>
    <div class="post-logo" style="left:110px;top:14px;color:#fff"><span class="name">Lorvu</span><span class="sub">Hair Design</span></div>
    <div class="rental-box">Chair Rental<br>Available</div>
    <div class="rental-band"></div>
    <div class="post-url" style="top:246px;color:var(--charcoal)">www.lorvuhairstudio.example</div>
  </article>

  <article class="post review-post">
    <div class="post-logo" style="left:13px;top:14px;color:var(--charcoal)"><span class="name">Lorvu</span><span class="sub">Hair Design</span></div>
    <div class="flourish" role="img" aria-label="Faint line flourish ornament" style="left:150px;top:35px;width:110px;height:60px;background:radial-gradient(ellipse,rgba(158,170,148,.35),transparent 70%)"></div>
    <div class="quote-mark" style="left:36px;top:76px">&ldquo;</div>
    <div class="quote-box">
      <p class="quote-text">&ldquo;The most transformative cut I have ever had &ndash; my stylist truly listened and the result feels effortless yet polished. I leave every visit feeling like a better version of myself.&rdquo;</p>
      <div class="quote-stars">★★★★★</div>
      <div class="quote-rule"></div>
      <div class="quote-name">ELENA R., REGULAR CLIENT SINCE 2021</div>
    </div>
    <div class="quote-mark" style="left:195px;top:182px">&rdquo;</div>
    <div class="post-url" style="top:250px;color:#a9b1a3">www.lorvuhairstudio.example</div>
  </article>

</div>
</body>
</html>
```